Business card for education consultant company

I need a business card created for my company. The company name is RW42 Learning Pathways Collective.

Marla J. Prewitt, Ed.D.
Founder and CEO
301-555-0187

```html
<!DOCTYPE html>
<html lang="en">
<head>
<meta charset="utf-8">
<title>RW42 Learning Pathways Collective – Business Card</title>
<link rel="stylesheet" href="https://fonts.googleapis.com/css2?family=Montserrat:wght@400;500;700&display=swap">
<style>
  :root {
    --stage: #1b1b1d;
    --brand-blue: #1f5f8b;
    --brand-green: #5cb84a;
    --paper: #f4f4f2;
    --ink: #1c2a44;
    --light-ink: #ffffff;
  }
  * { box-sizing: border-box; margin: 0; padding: 0; }
  html, body {
    width: 1200px; height: 900px; overflow: hidden;
    background: var(--stage);
    font-family: "Montserrat", sans-serif;
  }
  .stage { position: relative; width: 1200px; height: 900px; }

  .card {
    position: absolute;
    border-radius: 22px;
    overflow: hidden;
    background: var(--paper);
    box-shadow: 0 18px 40px rgba(0,0,0,.55);
  }

  /* Contact side (portrait) */
  .card--contact { left: 150px; top: 170px; width: 330px; height: 560px; }
  .contact__top-band { position: absolute; left: 0; top: 0; width: 100%; height: 42px; background: var(--brand-blue); }
  .contact__logo { position: absolute; left: 30px; top: 82px; width: 270px; }
  .contact__identity { position: absolute; left: 30px; top: 206px; right: 14px; }
  .contact__name { font-weight: 700; font-size: 20px; color: var(--ink); white-space: nowrap; }
  .contact__role { font-weight: 400; font-size: 15px; color: var(--ink); margin-top: 6px; }
  .contact__panel { position: absolute; left: 0; top: 290px; width: 100%; height: 270px; }
  .contact__list { position: absolute; left: 30px; top: 345px; right: 14px; list-style: none; }
  .contact__item {
    display: flex; align-items: center; gap: 9px;
    color: var(--light-ink); font-size: 13px; font-weight: 500;
    margin-bottom: 26px; white-space: nowrap;
  }
  .contact__item--phone { font-size: 14px; }
  .contact__item--email { font-size: 10.5px; }
  .contact__icon { width: 18px; height: 18px; flex: none; }

  /* Brand side (landscape) */
  .card--brand { left: 560px; top: 250px; width: 520px; height: 320px; }
  .brand__top-band { position: absolute; left: 0; top: 0; width: 100%; height: 44px; background: var(--brand-blue); }
  .brand__bottom { position: absolute; left: 0; bottom: 0; width: 100%; height: 110px; }
  .brand__logo { position: absolute; left: 0; top: 80px; width: 100%; text-align: center; }
  .brand__url {
    position: absolute; left: 42px; bottom: 36px;
    color: var(--light-ink); font-size: 15px; font-weight: 500;
  }

  .logo-mark { display: inline-flex; align-items: center; gap: 12px; }
  .logo-mark__dot { width: 26px; height: 26px; border-radius: 50%; background: var(--brand-green); flex: none; }
  .logo-mark__name {
    color: var(--brand-green); font-weight: 700; line-height: 1.15;
    text-align: left;
  }
  .contact__logo .logo-mark__name { font-size: 19px; }
  .brand__logo .logo-mark__name { font-size: 27px; }
  .brand__logo .logo-mark__dot { width: 34px; height: 34px; }
</style>
</head>
<body>
<main class="stage">

  <section class="card card--contact" aria-label="Business card, contact side">
    <div class="contact__top-band"></div>
    <div class="contact__logo">
      <div class="logo-mark">
        <span class="logo-mark__dot"></span>
        <span class="logo-mark__name">RW42 Learning<br>Pathways Collective</span>
      </div>
    </div>
    <div class="contact__identity">
      <p class="contact__name">Marla J. Prewitt, Ed.D.</p>
      <p class="contact__role">Founder and CEO</p>
    </div>
    <svg class="contact__panel" viewBox="0 0 330 270" preserveAspectRatio="none" aria-hidden="true">
      <path d="M0 0 H330 V270 H0 Z" fill="var(--brand-blue)"/>
      <path d="M150 0 L165 14 L180 0 Z" fill="var(--paper)"/>
    </svg>
    <ul class="contact__list">
      <li class="contact__item contact__item--phone">
        <svg class="contact__icon" viewBox="0 0 20 20"><circle cx="10" cy="10" r="10" fill="#fff"/><path d="M7 5.5 L8.6 5.5 L9.3 8 L8.3 8.9 Q9.3 11 11.1 11.8 L12 10.8 L14.5 11.5 L14.5 13 Q14 14.5 12.5 14.5 Q6 13.5 5.5 7.5 Q5.5 6 7 5.5 Z" fill="var(--brand-blue)"/></svg>
        301-555-0187
      </li>
      <li class="contact__item contact__item--email">
        <svg class="contact__icon" viewBox="0 0 20 20"><circle cx="10" cy="10" r="10" fill="#fff"/><rect x="5" y="6.5" width="10" height="7" rx="1" fill="var(--brand-blue)"/><path d="M5.3 7 L10 10.5 L14.7 7" stroke="#fff" stroke-width="1" fill="none"/></svg>
        rw42learningpathwayscollective@mbx.net
      </li>
      <li class="contact__item">
        <svg class="contact__icon" viewBox="0 0 20 20"><circle cx="10" cy="10" r="10" fill="#fff"/><circle cx="10" cy="10" r="5" fill="none" stroke="var(--brand-blue)" stroke-width="1.3"/><ellipse cx="10" cy="10" rx="2.2" ry="5" fill="none" stroke="var(--brand-blue)" stroke-width="1.1"/><path d="M5 10 H15" stroke="var(--brand-blue)" stroke-width="1.1"/></svg>
        http://www.rw42lpc.com
      </li>
    </ul>
  </section>

  <section class="card card--brand" aria-label="Business card, brand side">
    <div class="brand__top-band"></div>
    <div class="brand__logo">
      <div class="logo-mark">
        <span class="logo-mark__dot"></span>
        <span class="logo-mark__name">RW42 Learning<br>Pathways Collective</span>
      </div>
    </div>
    <svg class="brand__bottom" viewBox="0 0 520 110" preserveAspectRatio="none" aria-hidden="true">
      <path d="M0 50 H22 Q22 22 44 22 H250 Q270 22 270 42 Q270 50 285 50 H520 V110 H0 Z" fill="var(--brand-blue)"/>
    </svg>
    <p class="brand__url">http://www.rw42lpc.com</p>
  </section>

</main>
</body>
</html>
```